Keystone Trade Show Banners

Task Description:
We would like to see some design options for 2 different types of Trade Show banner designs. Size 2ft width X 8ft length. One banner design is a focus on our core Keystone business, and the second is a focus on our Rewards Loyalty Program. The content and images that we enjoy using on our collateral can be found on our corporate site www.ksnq.example and I will upload a few examples to reference for what we are looking for. The puzzle piece in the imagery uploaded is a core piece of our marketing and we are looking for designs that pop and are more professional in appearance than what has been created so far.

Company Information:
Keystone Supply Network is an exciting and fast-growing organization that connects OEM Wholesale Parts Suppliers with automotive industry customers; Repair Shops, Body Shops, Vehicle Manufacturers, and Auto Insurers. We have a long history of attracting and retaining talented individuals that are passionate about our Clients' success.
Our Keystone Perks program allows Repair Shops to earn Reward Points from multiple OEM Wholesale Parts Suppliers – not just one. How does it work?
Supplier Clients issue Reward Points to Shop Customers based on their purchases, account standing and special promotions - this means no wasted marketing costs. Suppliers are not required to issue Reward Points to every Shop — giving them flexibility and control.
Reward Points can really add up for the Shop, increasing loyalty and providing incentives for continued and increased OEM Wholesale Parts purchases.
Keystone Perks is aimed at increasing OEM Wholesale Parts sales by locking in your Shops.

Target Market(s)

Automotive Suppliers, Vehicle Manufacturers, Automotive Trade Shows

Font styles to use
Other font styles liked:
• Roboto

Requirements
Must have
• The puzzle piece image see in the examples
• Background is white
• Color palette should be black, grey and reds as seen in examples

```html
<!DOCTYPE html>
<html lang="en">
<head>
<meta charset="utf-8">
<title>Keystone Trade Show Banners</title>
<link href="https://fonts.googleapis.com/css2?family=Roboto:ital,wght@0,700;0,900;1,700&family=Roboto+Condensed:wght@700&display=swap" rel="stylesheet">
<style>
  :root {
    --stage: #e6e6e6;
    --white: #ffffff;
    --ink: #222222;
    --red: #c8102e;
    --black: #1a1a1a;
    --grey-dark: #3a3d42;
    --grey-light: #d9dcdf;
  }
  * { margin: 0; padding: 0; box-sizing: border-box; }
  html, body { width: 1200px; height: 1000px; overflow: hidden; }
  body {
    background: var(--stage);
    position: relative;
    font-family: "Roboto", Arial, sans-serif;
  }
  .banner {
    position: absolute;
    top: 30px;
    width: 233px;
    height: 935px;
    background: var(--white);
    box-shadow: 0 2px 8px rgba(0,0,0,0.25);
    overflow: hidden;
  }
  .banner--perks { left: 287px; }
  .banner--core { left: 637px; }

  .brand {
    position: absolute;
    top: 38px;
    left: 0;
    width: 100%;
    text-align: center;
  }
  .brand__dot {
    width: 64px;
    height: 64px;
    border-radius: 50%;
    background: var(--red);
    margin: 0 auto 10px;
  }
  .brand__name {
    font-family: "Roboto", Arial, sans-serif;
    font-weight: 900;
    font-size: 17px;
    line-height: 19px;
    letter-spacing: 1px;
    color: var(--black);
    text-transform: uppercase;
  }

  .headline {
    position: absolute;
    top: 208px;
    left: 0;
    width: 100%;
    text-align: center;
    font-family: "Roboto Condensed", "Arial Narrow", sans-serif;
    font-weight: 700;
    font-size: 22px;
    line-height: 29px;
    color: var(--ink);
  }

  .photo { position: absolute; left: 0; width: 100%; }
  .photo--resort {
    top: 360px;
    height: 225px;
    background: linear-gradient(180deg, #ffffff 0%, #e7f1f7 25%, #9fcfe3 48%, #5fb3cf 55%, #e9e4dc 66%, #b78e6a 82%, #efece7 100%);
  }
  .photo--shoppers {
    top: 585px;
    height: 215px;
    background: linear-gradient(160deg, #f3d9b8 0%, #d9b58b 30%, #9fb0c2 55%, #6f93ba 75%, #c96a5d 100%);
  }
  .photo--puzzle {
    top: 390px;
    height: 410px;
    background:
      radial-gradient(ellipse at 62% 45%, #d3202e 0%, #b5121f 22%, rgba(181,18,31,0) 42%),
      linear-gradient(180deg, #ffffff 0%, #e4e6e8 20%, #9a9ea3 55%, #3a3d42 85%, #c9cbcd 100%);
  }

  .footer {
    position: absolute;
    left: 0;
    bottom: 0;
    width: 100%;
    height: 175px;
  }
  .footer svg { display: block; width: 100%; height: 100%; }
  .footer__url {
    position: absolute;
    left: 0;
    bottom: 43px;
    width: 100%;
    text-align: center;
    font-family: "Roboto", Arial, sans-serif;
    font-weight: 700;
    font-style: italic;
    font-size: 19px;
    color: var(--white);
  }
</style>
</head>
<body>

  <section class="banner banner--perks">
    <div class="brand">
      <div class="brand__dot"></div>
      <div class="brand__name">Keystone<br>Supply Network</div>
    </div>
    <h2 class="headline">National OEM Parts<br>Loyalty Programme<br>for Suppliers<br>and their Customers</h2>
    <div class="photo photo--resort" role="img" aria-label="Sun loungers beside an infinity pool overlooking the sea"></div>
    <div class="photo photo--shoppers" role="img" aria-label="Happy couple with shopping bags on a sunny street"></div>
    <div class="footer">
      <svg viewBox="0 0 233 175" preserveAspectRatio="none" aria-hidden="true">
        <path d="M0 30 Q110 20 233 0 L233 175 L0 175 Z" fill="var(--black)"/>
        <path d="M0 46 Q110 36 233 14 L233 175 L0 175 Z" fill="var(--red)"/>
        <path d="M0 54 Q110 44 233 22 L233 26 Q110 48 0 58 Z" fill="var(--white)"/>
      </svg>
      <div class="footer__url">www.ksnq.example</div>
    </div>
  </section>

  <section class="banner banner--core">
    <div class="brand">
      <div class="brand__dot"></div>
      <div class="brand__name">Keystone<br>Supply Network</div>
    </div>
    <h2 class="headline">The Industry’s<br>Leading OEM<br>Parts Sales<br>And Marketing<br>Solutions Provider</h2>
    <div class="photo photo--puzzle" role="img" aria-label="Red puzzle piece lifting out of a black and grey jigsaw"></div>
    <div class="footer">
      <svg viewBox="0 0 233 175" preserveAspectRatio="none" aria-hidden="true">
        <path d="M0 30 Q110 20 233 0 L233 175 L0 175 Z" fill="var(--black)"/>
        <path d="M0 46 Q110 36 233 14 L233 175 L0 175 Z" fill="var(--red)"/>
        <path d="M0 54 Q110 44 233 22 L233 26 Q110 48 0 58 Z" fill="var(--white)"/>
      </svg>
      <div class="footer__url">www.ksnq.example</div>
    </div>
  </section>

</body>
</html>
```